Curbnest - Portable Skateboard Display, Organizer, & Stand

Single Webpage for a new company that just launched our first product, the "Curbnest Skateboard Stand". This is a consumer product targeted toward parents (especially moms) with kids who have skateboards laying around. Our product is a storage/display/stand that keeps skateboards off of the ground and wheels away from walls. The website design needs to really sell the product as a Portable and Quality product, which can be put anywhere in the home. The website should appeal to adults (Moms especially) and help them quickly understand the versatility, flexibility, high quality, simplicity, and use of the Curbnest Skateboard stand. Our website can be viewed at www.curbnest-example.company - we'd like to continue to link visitors to our Vendora product listing for purchases (in the design you submit). Please review the attached creative files and feel free to reach out for additional information.

Target Market(s)

Parents (specifically Moms) with children who own skateboards, interested in keeping a clean and organized home.

Industry/Entity Type

It Company

Number of Pages Required

1 page

Font styles to use
Sans Serif

Requirements
Must have
• Must express the Portability, Quality, and Flexibility of the product. (It can be moved / placed anywhere, does not require mounting or drilling holes)
Nice to have
• Really sell the ease of use and benefit.
Should not have
• Should not be overly complex or cluttered.

```html
<!DOCTYPE html>
<html lang="en">
<head>
<meta charset="utf-8">
<title>Curbnest - Portable Skateboard Display, Organizer, &amp; Stand</title>
<link href="https://fonts.googleapis.com/css2?family=Oswald:wght@400;500;600;700&family=Open+Sans:wght@400;600;700&display=swap" rel="stylesheet">
<style>
:root{
  --orange:#f7941d;
  --orange-deep:#f26522;
  --red:#e8313a;
  --blue:#1b7ed6;
  --ink:#2c2c2c;
  --dark:#303030;
  --darker:#262626;
  --grey:#8a8a8a;
  --light:#f1f1f1;
  --line:#e2e2e2;
  --white:#ffffff;
}
*{box-sizing:border-box;margin:0;padding:0}
html,body{width:1200px;height:2984px;overflow:hidden}
body{font-family:"Open Sans",Arial,sans-serif;color:var(--ink);background:var(--white);position:relative}
.head{font-family:"Oswald","Arial Narrow",sans-serif;text-transform:uppercase}

/* top bar */
.topbar{height:32px;background:var(--white);border-bottom:1px solid var(--line);display:flex;align-items:center;padding:0 112px;justify-content:space-between;font-size:11px;color:var(--grey)}
.search{width:260px;height:20px;border:1px solid var(--line);padding:0 8px;line-height:18px}
/* header */
.header{height:72px;background:var(--darker);display:flex;align-items:stretch;padding:0 0 0 10px}
.brand{display:flex;align-items:center;gap:10px;width:250px}
.brand-mark{width:34px;height:34px;background:var(--blue)}
.brand-name{font-family:"Open Sans",sans-serif;font-weight:700;font-size:26px;color:var(--white)}
.nav{display:flex;align-items:stretch;flex:1}
.nav a{font-family:"Oswald",sans-serif;font-size:13px;color:var(--white);text-decoration:none;padding:0 18px;display:flex;align-items:center;text-transform:uppercase}
.nav a.active{background:var(--orange)}
.header-right{display:flex;align-items:stretch}
.header-right a{font-family:"Oswald",sans-serif;font-size:13px;color:var(--white);padding:0 20px;display:flex;align-items:center;text-decoration:none}
.cart{background:var(--orange);gap:8px}
.cart-dot{width:16px;height:16px;border-radius:50%;background:var(--white)}

/* hero */
.hero{position:relative;height:384px;background:linear-gradient(180deg,#6f8ca8 0%,#b6c5cf 55%,#6b6a5a 80%,#3a3a33 100%);overflow:hidden}
.hero-photo{position:absolute;inset:0}
.hero-title{position:absolute;left:390px;top:175px;display:flex;align-items:center;gap:0}
.hero-left{background:var(--orange);color:var(--white);padding:10px 18px;font-family:"Oswald",sans-serif;font-weight:700;font-size:30px;line-height:1;text-align:right}
.hero-right{background:var(--white);color:var(--ink);padding:8px 18px;font-family:"Oswald",sans-serif;font-weight:700;font-size:52px;line-height:1}
.hero-arrow{position:absolute;top:170px;color:var(--white);font-size:40px;font-family:"Oswald",sans-serif}
.hero-dots{position:absolute;bottom:18px;left:50%;transform:translateX(-50%);display:flex;gap:8px}
.hero-dots span{width:10px;height:10px;border-radius:50%;background:rgba(255,255,255,.6)}
.hero-dots span.on{background:var(--orange)}

/* promo */
.promo{position:relative;margin:32px 0 0 228px;width:852px;height:240px}
.promo-ship{position:absolute;left:0;top:0;width:364px;height:240px;background:linear-gradient(90deg,var(--red),var(--orange));overflow:hidden}
.promo-ship .prod{position:absolute;left:14px;top:70px;width:120px;height:140px;background:linear-gradient(180deg,#3a3a3a,#f0d020);border-radius:6px}
.promo-ship .txt{position:absolute;right:20px;top:68px;color:var(--white);font-family:"Oswald",sans-serif;font-weight:700;text-transform:uppercase;font-size:40px;line-height:1;text-align:right}
.promo-ship .txt small{display:block;font-size:16px;font-weight:500;margin-top:6px}
.promo-new{position:absolute;left:376px;top:0;width:196px;height:240px}
.promo-new .prod{position:absolute;left:10px;top:70px;width:170px;height:150px;background:linear-gradient(180deg,#444,#9ad23a);border-radius:6px}
.badge{position:absolute;left:0;top:12px;width:80px;height:80px;border-radius:50%;background:var(--orange);color:var(--white);font-family:"Oswald",sans-serif;font-weight:700;text-align:center;padding-top:18px;font-size:13px;line-height:1.2}
.badge b{display:block;font-size:20px}
.promo-bulk{position:absolute;left:592px;top:10px;width:260px}
.promo-bulk h2{font-family:"Oswald",sans-serif;font-weight:700;font-size:46px;line-height:1}
.promo-bulk h3{font-family:"Oswald",sans-serif;font-weight:500;font-size:32px;line-height:1.05}
.promo-bulk p{font-family:"Oswald",sans-serif;font-size:18px;margin-top:4px}
.promo-bulk p b{color:var(--orange);font-size:22px}
.btn{display:inline-block;background:var(--blue);color:var(--white);font-family:"Oswald",sans-serif;font-size:15px;text-transform:uppercase;text-align:center;line-height:46px;height:46px}
.promo-bulk .btn{width:240px;margin-top:20px}

/* collections */
.collections{position:relative;height:400px;margin-top:28px}
.coll-bg{position:absolute;inset:0}
.sec-head{display:flex;justify-content:space-between;align-items:center;border-bottom:2px solid var(--line);padding-bottom:6px}
.sec-head h2{font-family:"Oswald",sans-serif;font-weight:600;font-size:18px;color:var(--orange);text-transform:uppercase}
.arrows{display:flex;gap:4px}
.arrows span{width:20px;height:20px;background:#dcdcdc;color:var(--white);font-size:12px;text-align:center;line-height:20px}
.arrows span.on{background:var(--orange)}
.coll-inner{position:relative;margin-left:228px;width:852px;padding-top:12px}
.cards{display:flex;gap:16px;margin-top:20px}
.card{width:201px;height:292px;background:var(--white);border:1px solid var(--line);padding:14px}
.card.featured{background:var(--orange);border-color:var(--orange)}
.card .img{height:190px;border-radius:4px}
.card .meta{display:flex;justify-content:space-between;align-items:flex-start;margin-top:12px;font-family:"Oswald",sans-serif;font-size:12px;line-height:1.2;text-transform:uppercase}
.card .price{font-size:18px;font-weight:500}
.card .buy{font-size:11px;color:var(--grey);margin-top:10px}
.card.featured .meta,.card.featured .buy{color:var(--white)}

/* news band */
.news{height:380px;margin-top:0;background:linear-gradient(180deg,#4b4a47,#2e2d2b);position:relative;text-align:center;color:var(--white);padding-top:110px}
.news h2{font-family:"Oswald",sans-serif;font-weight:500;font-size:32px;line-height:1.25;text-transform:uppercase}
.news p{font-size:11px;color:#d0d0d0;margin-top:20px}
.subscribe{display:flex;justify-content:center;margin-top:16px}
.subscribe .field{width:440px;height:46px;background:var(--white);color:var(--grey);font-size:13px;text-align:left;padding-left:16px;line-height:46px}
.subscribe .btn{width:220px}

/* features */
.features{margin:20px 112px 0;height:240px;background:var(--orange);display:flex;padding:32px 20px}
.feature{flex:1;text-align:center;color:var(--white);padding:0 20px;border-right:1px solid rgba(255,255,255,.4)}
.feature:last-child{border-right:0}
.icon{width:64px;height:64px;border-radius:50%;background:var(--white);margin:0 auto;display:flex;align-items:center;justify-content:center}
.feature h3{font-family:"Oswald",sans-serif;font-weight:500;font-size:15px;text-transform:uppercase;margin-top:16px}
.feature p{font-size:11px;line-height:1.5;margin-top:8px}

/* testimonials */
.say{margin:40px 112px 0;height:220px}
.quotes{position:relative;height:150px;margin-top:28px}
.quote{position:absolute;top:0;height:140px;display:flex;background:var(--white)}
.quote.side{opacity:.35}
.quote .face{width:120px;height:140px;background:linear-gradient(180deg,var(--orange),var(--orange-deep))}
.quote .body{padding:18px 24px;width:300px;font-size:11px;color:var(--grey);line-height:1.6;border:1px solid var(--line);border-left:0}
.quote .mark{font-family:Georgia,serif;font-size:40px;color:#cfcfcf;line-height:.6;display:block}
.quote .name{color:var(--orange);font-weight:600;margin-top:6px}
.dots{display:flex;justify-content:center;gap:6px}
.dots span{width:8px;height:8px;border-radius:50%;background:#cccccc}
.dots span.on{background:var(--orange)}

/* blog */
.blog{margin:28px 112px 0;height:400px}
.posts{display:flex;gap:22px;margin-top:20px}
.post{width:311px}
.post .img{height:200px}
.post h3{font-family:"Oswald",sans-serif;font-weight:600;font-size:16px;line-height:1.25;text-transform:uppercase;margin-top:14px}
.post .date{font-size:10px;color:var(--orange);margin-top:6px}
.post p{font-size:10px;color:var(--grey);line-height:1.5;margin-top:4px}

/* footer */
.footer{position:absolute;left:0;top:2560px;width:1200px;height:424px}
.footer svg{position:absolute;inset:0}
.foot-inner{position:absolute;left:0;right:0;top:210px;text-align:center;color:#bdbdbd}
.socials{display:flex;justify-content:center;gap:10px}
.socials span{width:26px;height:26px;border-radius:50%;background:var(--white)}
.contact{font-family:"Oswald",sans-serif;font-size:12px;color:var(--white);margin-top:20px;line-height:1.6;text-transform:uppercase}
.pay{display:flex;justify-content:center;gap:8px;margin-top:14px}
.pay span{width:36px;height:20px;background:#555;border-radius:2px}
.copy{font-size:10px;margin-top:40px;color:#8d8d8d}
</style>
</head>
<body>

<div class="topbar">
  <div class="search">Search...</div>
  <div>Sign in &nbsp;|&nbsp; Register</div>
</div>

<header class="header">
  <div class="brand"><span class="brand-mark"></span><span class="brand-name">Curbnest</span></div>
  <nav class="nav">
    <a class="active" href="#">Home</a>
    <a href="#">Collections</a>
    <a href="#">Shop</a>
    <a href="#">Blog</a>
    <a href="#">Contact</a>
  </nav>
  <div class="header-right">
    <a href="#">Blog</a>
    <a class="cart" href="#">My Cart (0) <span class="cart-dot"></span></a>
  </div>
</header>

<section class="hero">
  <div class="hero-photo" role="img" aria-label="Photo of a young skater riding a longboard along a waterfront path under a cloudy sky"></div>
  <div class="hero-arrow" style="left:16px">&#8249;</div>
  <div class="hero-arrow" style="right:16px">&#8250;</div>
  <div class="hero-title">
    <div class="hero-left">KEEP YOUR<br>BOARD</div>
    <div class="hero-right">WHERE YOU WANT IT!</div>
  </div>
  <div class="hero-dots"><span class="on"></span><span></span><span></span><span></span></div>
</section>

<section class="promo">
  <div class="promo-ship">
    <div class="prod" role="img" aria-label="Skateboard resting in a Curbnest stand"></div>
    <div class="txt">Free Shipping<br>For Members<small>Order over $39</small></div>
  </div>
  <div class="promo-new">
    <div class="prod" role="img" aria-label="Green Curbnest stand holding a skateboard"></div>
    <div class="badge">NEW ARRIVAL<b>20% OFF</b></div>
  </div>
  <div class="promo-bulk">
    <h2>HOT PROMO</h2>
    <h3>BULK DISCOUNTS</h3>
    <p><b>40%</b> ENTIRE PURCHASE</p>
    <span class="btn">Explore Now</span>
  </div>
</section>

<section class="collections">
  <svg class="coll-bg" width="1200" height="400" viewBox="0 0 1200 400">
    <polygon points="0,150 460,60 700,400 0,400" fill="#e9e9e9"/>
    <polygon points="800,400 1200,120 1200,400" fill="#dedede"/>
  </svg>
  <div class="coll-inner">
    <div class="sec-head"><h2>Collections</h2><div class="arrows"><span>&#8249;</span><span class="on">&#8250;</span></div></div>
    <div class="cards">
      <div class="card">
        <div class="img" role="img" aria-label="Grey Curbnest stand with a skateboard" style="background:linear-gradient(180deg,#333,#8e8e8e)"></div>
        <div class="meta"><span>Grey<br>Curbnest Stand</span><span class="price">$19.95</span></div>
        <div class="buy">Buy on Vendora</div>
      </div>
      <div class="card">
        <div class="img" role="img" aria-label="Green Curbnest stand with a skateboard" style="background:linear-gradient(180deg,#333,#8fd13a)"></div>
        <div class="meta"><span>Green<br>Curbnest Stand</span><span class="price">$19.95</span></div>
        <div class="buy">Buy on Vendora</div>
      </div>
      <div class="card featured">
        <div class="img" role="img" aria-label="White Curbnest stand with a skateboard" style="background:linear-gradient(180deg,#f6b86a,#fde7c9)"></div>
        <div class="meta"><span>White<br>Curbnest Stand</span><span class="price">$19.95</span></div>
        <div class="buy">Buy on Vendora</div>
      </div>
      <div class="card">
        <div class="img" role="img" aria-label="Red Curbnest stand with a skateboard" style="background:linear-gradient(180deg,#333,#e0304a)"></div>
        <div class="meta"><span>Red<br>Curbnest Stand</span><span class="price">$19.95</span></div>
        <div class="buy">Buy on Vendora</div>
      </div>
    </div>
  </div>
</section>

<section class="news" role="img" aria-label="Dark background photo of skaters at a festival">
  <h2>The most recent incarnation of the KSF greets Indonesia<br>while 45 skaters participate at this year's flagship festival</h2>
  <p>Join our mailing list and get news, events and special offers sent to your inbox first.</p>
  <div class="subscribe"><div class="field">Email</div><span class="btn">Subscribe</span></div>
</section>

<section class="features">
  <div class="feature">
    <div class="icon"><svg width="30" height="22" viewBox="0 0 30 22"><rect x="1" y="3" width="17" height="12" fill="none" stroke="#f7941d" stroke-width="2"/><path d="M18 7h6l4 4v4h-10z" fill="none" stroke="#f7941d" stroke-width="2"/><circle cx="7" cy="18" r="3" fill="#f7941d"/><circle cx="23" cy="18" r="3" fill="#f7941d"/></svg></div>
    <h3>Fast Delivery</h3>
    <p>Orders ship within one business day and arrive quickly at your door.</p>
  </div>
  <div class="feature">
    <div class="icon"><svg width="24" height="28" viewBox="0 0 24 28"><rect x="2" y="12" width="20" height="14" fill="#f7941d"/><path d="M6 12V8a6 6 0 0 1 12 0v4" fill="none" stroke="#f7941d" stroke-width="2.5"/></svg></div>
    <h3>Secure Payment</h3>
    <p>Every checkout is encrypted so your details always stay safe.</p>
  </div>
  <div class="feature">
    <div class="icon"><svg width="28" height="28" viewBox="0 0 28 28"><circle cx="14" cy="14" r="11" fill="none" stroke="#f7941d" stroke-width="2.5"/><path d="M14 7v7l5 3" fill="none" stroke="#f7941d" stroke-width="2.5"/></svg></div>
    <h3>24/7 Support</h3>
    <p>Our friendly team is here to help you any time of the day.</p>
  </div>
  <div class="feature">
    <div class="icon"><svg width="28" height="28" viewBox="0 0 28 28"><path d="M2 13a12 10 0 0 1 24 0z" fill="#f7941d"/><path d="M14 13v10a3 3 0 0 1-6 0" fill="none" stroke="#f7941d" stroke-width="2.5"/></svg></div>
    <h3>Protected Package</h3>
    <p>Each stand is packed with care so it reaches you in perfect shape.</p>
  </div>
</section>

<section class="say">
  <div class="sec-head"><h2>What They Say?</h2><div class="arrows"><span>&#8249;</span><span class="on">&#8250;</span></div></div>
  <div class="quotes">
    <div class="quote side" style="left:-60px"><div class="body" style="border-left:1px solid #e2e2e2"><span class="mark">&ldquo;</span>The stand keeps the hallway tidy and the walls clean.</div></div>
    <div class="quote" style="left:268px">
      <div class="face" role="img" aria-label="Portrait photo of a customer"></div>
      <div class="body"><span class="mark">&ldquo;</span>Finally the boards are off the floor. My kids park them in the stand every day and the walls stay clean.<div class="name">Dana Rowe</div></div>
    </div>
    <div class="quote side" style="left:760px"><div class="face" role="img" aria-label="Portrait photo of a customer"></div></div>
  </div>
  <div class="dots"><span></span><span></span><span class="on"></span><span></span><span></span><span></span><span></span></div>
</section>

<section class="blog">
  <div class="sec-head"><h2>From The Blog</h2><div class="arrows"><span>&#8249;</span><span class="on">&#8250;</span></div></div>
  <div class="posts">
    <article class="post">
      <div class="img" role="img" aria-label="Photo of a bright garage entry used for storage" style="background:linear-gradient(135deg,#8aa07a,#d8d4c8)"></div>
      <h3>Storage area for tools and accessories</h3>
      <div class="date">May 12, 2017</div>
      <p>Keep boards, helmets and pads in one neat spot the whole family can find.</p>
    </article>
    <article class="post">
      <div class="img" role="img" aria-label="Photo of skateboards standing upright in a hallway" style="background:linear-gradient(135deg,#6b5444,#d9cfc2)"></div>
      <h3>Keep wheels away from walls - no more marks!</h3>
      <div class="date">May 08, 2017</div>
      <p>Wheels stay lifted off the floor so paint and baseboards stay clean.</p>
    </article>
    <article class="post">
      <div class="img" role="img" aria-label="Photo of a skateboard stand by a front door" style="background:linear-gradient(135deg,#9aa7a8,#e4e0d6)"></div>
      <h3>Portable and easy to move - no mounting or drilling!</h3>
      <div class="date">May 02, 2017</div>
      <p>Set it anywhere in the home and move it whenever you like.</p>
    </article>
  </div>
</section>

<footer class="footer">
  <svg width="1200" height="424" viewBox="0 0 1200 424">
    <polygon points="0,40 1200,0 1200,424 0,424" fill="#e6e6e6"/>
    <polygon points="0,150 1200,110 1200,424 0,424" fill="#2e2e2e"/>
  </svg>
  <div class="foot-inner">
    <div class="socials"><span></span><span></span><span></span><span></span><span></span><span></span></div>
    <div class="contact">Contact<br>Curbnest Co. &middot; 410 Harbor Lane, Suite 12, Bayview, CA 90000<br>1 555 0100 2000</div>
    <div class="pay"><span></span><span></span><span></span><span></span></div>
    <div class="copy">&copy; 2017 Curbnest. All rights reserved. www.curbnest-example.company</div>
  </div>
</footer>

</body>
</html>
```